Podcast Cover Art for Fast Growing Show (Ill include a gracious tip!)

This artwork is for "The Steadfast Fellow Show." The podcast is for men, and it's all about self-improvement, confidence, success, money, women and masculinity. It's for the guy who wants to improve himself. I'd like for my picture to be included — in black and white — and I want the text to read: "The Steadfast Fellow Show" and somewhere in there it'll say: "with Dale Prowen." I'm open to color schemes. The podcast is a little edgy so I'd like for that to be represented in the design. Thank you! (((Here's the podcast page if you wanna check it out: http://steadfastfellowshow.castorbit.net/)))

Target Market(s)

Men who want to attract women and improve their lives!

Font styles to use
Serif

Colors

Designer to choose colors to be used in the design.

Requirements
Must have
• My image in it (in black and white) and the two titles: "The Steadfast Fellow Show" and "with Dale Prowen"
Nice to have
• My logo in it somehow (which is the arrow looking logo attached below). I've also found that my image looks best in black and white and with a circular type cut out (although I'm open to different design ideas). I've attached my logo with a circular cut out below so you can see what I'm talking about.
Should not have
• Flowers. Teddy bears. ice cream.

```html
<!DOCTYPE html>
<html lang="en">
<head>
<meta charset="utf-8">
<title>The Steadfast Fellow Show – Cover Art</title>
<link rel="stylesheet" href="https://fonts.googleapis.com/css2?family=Abril+Fatface&family=Bodoni+Moda:wght@800&family=Montserrat:wght@500&display=swap">
<style>
  :root {
    --ink: #000000;
    --paper: #ffffff;
    --signal-red: #e3222b;
    --ring: #151515;
    --portrait-light: #f2f2f2;
    --portrait-dark: #2a2a2a;
  }
  * { margin: 0; padding: 0; box-sizing: border-box; }
  html, body { width: 1200px; height: 1200px; overflow: hidden; background: var(--ink); }
  .cover {
    position: relative;
    width: 1200px;
    height: 1200px;
    background: var(--ink);
    border: 2px solid #3a3a3a;
    overflow: hidden;
  }
  .show-title {
    position: absolute;
    top: 62px;
    left: 0;
    width: 100%;
    text-align: center;
    font-family: "Abril Fatface", serif;
    font-size: 112px;
    line-height: 1;
    color: var(--signal-red);
    letter-spacing: -1px;
    transform: scaleX(0.86);
  }
  .show-subtitle {
    position: absolute;
    top: 198px;
    left: 0;
    width: 100%;
    text-align: center;
    font-family: "Bodoni Moda", serif;
    font-weight: 800;
    font-size: 66px;
    line-height: 1;
    color: var(--paper);
    letter-spacing: 30px;
    padding-left: 30px;
  }
  .band {
    position: absolute;
    top: 495px;
    left: 0;
    width: 100%;
    height: 210px;
    background: var(--paper);
  }
  .portrait-ring {
    position: absolute;
    left: 305px;
    top: 290px;
    width: 590px;
    height: 590px;
    border-radius: 50%;
    background: var(--ring);
  }
  .portrait {
    position: absolute;
    left: 325px;
    top: 310px;
    width: 550px;
    height: 550px;
    border-radius: 50%;
    background: radial-gradient(ellipse at 50% 30%, var(--portrait-light) 35%, #b5b5b5 55%, var(--portrait-dark) 85%);
  }
  .host-banner {
    position: absolute;
    left: 250px;
    top: 850px;
    width: 700px;
    height: 295px;
  }
  .host-name {
    position: absolute;
    top: 1010px;
    left: 250px;
    width: 700px;
    text-align: center;
    font-family: "Montserrat", sans-serif;
    font-weight: 500;
    font-size: 52px;
    line-height: 1;
    color: var(--paper);
  }
</style>
</head>
<body>
  <main class="cover">
    <h1 class="show-title">The Steadfast Fellow</h1>
    <p class="show-subtitle">SHOW</p>

    <div class="band"></div>
    <div class="portrait-ring"></div>
    <div class="portrait" role="img" aria-label="Black and white portrait of the host, hands steepled in front of his chin"></div>

    <svg class="host-banner" viewBox="0 0 700 295" aria-hidden="true">
      <path fill="var(--signal-red)" d="M6 118 L40 112 L120 104 L260 88 L420 66 L560 40 L650 20 L690 2 L694 60 L688 160 L692 230 L684 236 L520 250 L360 262 L200 274 L60 284 L36 290 L28 250 L22 190 L12 150 Z"/>
    </svg>
    <p class="host-name">with Dale Prowen.</p>
  </main>
</body>
</html>
```